Business Postcard Mailer - 2 sided - 6 x 10.5 inches

We will be purchasing multiple designs through this project. We need a postcard mailer for a residential painting business. The final design needs to have the special 15% Off, contact information, company logo, stamp indicia, and list of services. I will provide past examples and any additional logos. Company colors are #34482E and #4A1717. Old samples are provided. Final flat size should be 6 x 10.5 inches. And we will need a return address in the upper left-hand corner of the backside. USPS Layout Guidelines are attached. 4820 Fennel Ave #3, Waukesha, WI 53189.

I just guaranteed the project and will be expecting more entries. We will also be purchasing additional designs (4-5) so we want to ensure a good variety.

Target Market(s)

Homeowners

Industry/Entity Type

Painting

Font styles to use
Sans Serif

Requirements
Must have
• Logo and brand colors
Nice to have
• Call to action - Book your free estimate at www.BrightLoftPainting.com or Call now 262-555-0147.

```html
<!DOCTYPE html>
<html lang="en">
<head>
<meta charset="utf-8">
<title>Bright Loft Painting – Postcard Mailer</title>
<link rel="stylesheet" href="https://fonts.googleapis.com/css2?family=Montserrat:wght@400;500;600;700;800&display=swap">
<style>
  :root{
    --brand-green:#34482E;
    --brand-red:#4A1717;
    --pink:#E0226B;
    --white:#FFFFFF;
    --ink:#1E1E1E;
    --panel-grey:#D1D1D4;
    --panel-grey-dark:#BDBDC1;
    --sky-top:#8FB0C9;
    --sky-mid:#C9D6DE;
    --roof:#9B4A2E;
    --lawn:#5E6B38;
  }
  *{box-sizing:border-box;margin:0;padding:0}
  html,body{width:984px;height:1200px;overflow:hidden;background:var(--white)}
  body{font-family:"Montserrat",Arial,sans-serif;color:var(--ink);position:relative}

  /* ---------- FRONT ---------- */
  .front{position:absolute;left:0;top:0;width:984px;height:582px;overflow:hidden}
  .front-photo{position:absolute;inset:0;
    background:linear-gradient(180deg,var(--sky-top) 0%,var(--sky-mid) 30%,#B99A88 45%,var(--roof) 52%,#EDEDEA 62%,#6E6D5C 72%,var(--lawn) 82%,#485028 100%)}
  .ribbon-local{position:absolute;left:48px;top:28px;width:348px;height:30px;background:var(--pink);
    clip-path:polygon(0 0,100% 0,94% 100%,0 100%);color:var(--white);font-size:17px;font-weight:500;
    display:flex;align-items:center;padding-left:30px}
  .brand-front{position:absolute;left:48px;top:70px}
  .brand-front .brand-name{font-size:40px;font-weight:800;color:var(--brand-green);line-height:1.02;letter-spacing:-.3px}
  .brand-front .brand-phone{font-size:36px;font-weight:500;color:var(--brand-red);margin-top:8px;line-height:1}
  .brand-front .brand-web{font-size:20px;font-weight:700;color:var(--brand-green);margin-top:6px}
  .tagline{position:absolute;left:268px;top:468px;width:250px;text-align:center;color:var(--white);
    font-size:14px;line-height:1.3;text-shadow:0 1px 3px rgba(0,0,0,.6)}
  .offer{position:absolute;background:rgba(255,255,255,.88);text-align:center;color:var(--ink)}
  .offer-free{left:728px;top:30px;width:214px;height:86px;border:3px solid var(--pink);padding-top:12px}
  .offer-free .big{font-size:27px;font-weight:500;line-height:1}
  .offer-free .mid{font-size:13px;font-weight:500;letter-spacing:.3px;margin-top:2px}
  .offer-free .small{font-size:9px}
  .offer-sale{left:728px;top:133px;width:214px;height:86px;padding-top:14px}
  .offer-sale .big{font-size:28px;font-weight:500;line-height:1}
  .offer-sale .mid{font-size:13px;font-weight:500;margin-top:2px}
  .offer-sale .small{font-size:9px}
  .services-front{position:absolute;right:0;top:394px;width:378px}
  .services-front li{list-style:none;height:32px;margin-bottom:11.5px;background:var(--pink);color:var(--white);
    font-size:16.5px;font-weight:500;display:flex;align-items:center;justify-content:center;
    clip-path:polygon(0 0,100% 0,100% 100%,0 100%,5% 50%)}

  /* ---------- BACK ---------- */
  .back{position:absolute;left:0;top:617px;width:984px;height:583px;overflow:hidden;background:var(--white)}
  .back-shape{position:absolute;left:0;top:0}
  .brand-back{position:absolute;left:48px;top:44px;font-size:29px;font-weight:800;color:var(--brand-green);line-height:1.02}
  .return-address{position:absolute;left:62px;top:114px;font-size:13px;line-height:1.3;color:#333}
  .estimates{position:absolute;left:45px;top:170px}
  .estimates h2{font-size:20px;font-weight:700;letter-spacing:1px;color:#2A2A2A;margin-bottom:8px}
  .estimates li{list-style:none;font-size:13.5px;font-weight:600;line-height:22.5px;display:flex;align-items:center}
  .estimates li::before{content:"";width:22px;height:4px;border-radius:2px;background:var(--pink);margin-right:14px;transform:rotate(-6deg)}
  .badges{position:absolute;left:52px;top:292px;width:330px;height:110px}
  .badge{position:absolute;background:#8C8C90;opacity:.7}
  .cta{position:absolute;left:45px;top:443px}
  .cta h2{font-size:20px;font-weight:700;color:#2A2A2A;letter-spacing:.5px;margin-bottom:10px}
  .cta li{list-style:none;display:flex;align-items:center;font-size:15px;letter-spacing:1.4px;line-height:24px;color:#222}
  .cta svg{width:18px;height:18px;margin-right:16px;flex:none}
  .photo-circle{position:absolute;width:116px;height:116px;border-radius:50%;border:4px solid var(--white);
    box-shadow:0 0 0 6px var(--pink)}
  .photo-living-1{left:432px;top:87px;background:linear-gradient(160deg,#E9E7E3,#BFB8AE 55%,#5C5650)}
  .photo-living-2{left:404px;top:310px;background:linear-gradient(160deg,#EEEEEC,#CFCDC8 55%,#3D3B3A)}
  .indicia{position:absolute;left:706px;top:58px;width:107px;height:112px;border:2px solid #111;text-align:center;
    font-size:12px;line-height:1.3;padding-top:10px;color:#111}
  .indicia strong{display:block;font-size:15px;margin:4px 0 2px}
  .address-block{position:absolute;left:591px;top:233px;width:352px;height:230px;border:2px solid #111;border-radius:28px}
</style>
</head>
<body>

<section class="front">
  <div class="front-photo" role="img" aria-label="Photo of a large white Tudor-style house with a red tile roof and a green lawn, with a pink paint splash illustration at left"></div>

  <div class="ribbon-local">Locally Owend and Operated</div>

  <div class="brand-front">
    <div class="brand-name">Bright Loft<br>Painting</div>
    <div class="brand-phone">262-555-0147</div>
    <div class="brand-web">www.BrightLoftPainting.com</div>
  </div>

  <div class="offer offer-free">
    <div class="big">FREE</div>
    <div class="mid">COLOR CONSULTATIONS</div>
    <div class="small">with interior or exterior booked job</div>
  </div>
  <div class="offer offer-sale">
    <div class="big">15% OFF</div>
    <div class="mid">FALL SPECIAL</div>
    <div class="small">while openings are still available</div>
  </div>

  <p class="tagline">We cater the size of the crew to the size of the job and work full continuous days until the project is complete.</p>

  <ul class="services-front">
    <li>INTERIOR AND EXTERIOR PIANTING</li>
    <li>CARPENTRY SERVICES</li>
    <li>DRYWALL REPAIR</li>
    <li>COLOR CONSULTATIONS</li>
  </ul>
</section>

<section class="back">
  <svg class="back-shape" width="984" height="583" viewBox="0 0 984 583" aria-hidden="true">
    <path d="M0 0 H560 C500 120 470 260 440 380 C420 460 400 530 380 583 H0 Z" fill="var(--panel-grey)"/>
    <path d="M0 440 C140 400 300 380 410 410 L380 583 H0 Z" fill="var(--panel-grey-dark)"/>
    <path d="M560 0 C500 120 470 260 440 380 C420 460 400 530 380 583" fill="none" stroke="#E0226B" stroke-width="9"/>
    <path d="M0 440 C140 400 300 380 410 410" fill="none" stroke="#E0226B" stroke-width="9"/>
  </svg>

  <div class="brand-back">Bright Loft<br>Painting</div>
  <div class="return-address">4820 Fennel Ave #3<br>Waukesha, WI 53189</div>

  <div class="estimates">
    <h2>FREE ESTIMATES</h2>
    <ul>
      <li>INTERIOR AND EXTERIOR PIANTING</li>
      <li>CARPENTRY SERVICES</li>
      <li>DRYWALL REPAIR</li>
      <li>COLOR CONSULTATIONS</li>
    </ul>
  </div>

  <div class="badges" aria-label="Trade association memberships">
    <span class="badge" style="left:55px;top:0;width:42px;height:46px;border-radius:4px"></span>
    <span class="badge" style="left:195px;top:0;width:70px;height:48px;border-radius:4px"></span>
    <span class="badge" style="left:0;top:68px;width:74px;height:32px;border-radius:4px"></span>
    <span class="badge" style="left:92px;top:68px;width:62px;height:32px;border-radius:4px"></span>
    <span class="badge" style="left:170px;top:66px;width:52px;height:36px;border-radius:4px"></span>
    <span class="badge" style="left:238px;top:62px;width:66px;height:40px;border-radius:4px"></span>
  </div>

  <div class="cta">
    <h2>CALL OR EMAIL TODAY!</h2>
    <ul>
      <li><svg viewBox="0 0 24 24"><path d="M6.6 10.8a15 15 0 0 0 6.6 6.6l2.2-2.2a1 1 0 0 1 1-.25 11.4 11.4 0 0 0 3.6.57 1 1 0 0 1 1 1V20a1 1 0 0 1-1 1A17 17 0 0 1 3 4a1 1 0 0 1 1-1h3.5a1 1 0 0 1 1 1 11.4 11.4 0 0 0 .57 3.6 1 1 0 0 1-.25 1z" fill="#222"/></svg>262-555-0147</li>
      <li><svg viewBox="0 0 24 24"><circle cx="12" cy="12" r="9" fill="none" stroke="#222" stroke-width="2"/><path d="M3 12h18M12 3c3 3 3 15 0 18M12 3c-3 3-3 15 0 18" fill="none" stroke="#222" stroke-width="1.6"/></svg>www.BrightLoftPainting.com</li>
      <li><svg viewBox="0 0 24 24"><rect x="2" y="5" width="20" height="14" fill="#222"/><path d="M2 5l10 8 10-8" fill="none" stroke="#fff" stroke-width="1.6"/></svg>office@BrightLoftPainting.com</li>
    </ul>
  </div>

  <div class="photo-circle photo-living-1" role="img" aria-label="Photo of a bright living room with a grey sofa"></div>
  <div class="photo-circle photo-living-2" role="img" aria-label="Photo of a white interior with a black sofa and plants"></div>

  <div class="indicia">Presorted<br>Standard<br>U.S. Postage<strong>PAID</strong>PMC</div>
  <div class="address-block" aria-label="Mailing address area"></div>
</section>

</body>
</html>
```